Website Design for a New Business Sharing Application

Purpose: Website for a new product – a sharing application called "Gathr.io"

Product concept: Easy sharing of business information. The application has different sections: tasks, calendars, documents, contacts, notes and links. The key feature of the application is that you can drag and drop information from different sections into a "share." A share is a page which lists all the types of information that you drag into it. You can add people to this "share."

Note: The application itself is not part of this project, just the website.

Website details: The site, in addition to being informational, will actually be the first point of entry for visitors into the application itself. Because of that, we would like the website design to reflect the look of the application, to create a smooth and seamless experience for the user moving from the website into the application (tough the website does not need to look *exactly* like the application). Included Product Tour screenshots show you the look of the application.

Website pages to be created: 4 pages
We are flexible in terms of the exact structure and placement of elements. You may change that any way you like. The pages are as follows:

Home page
Product Tour page
Press page
Blog page

Specific description of pages are provided in project files we will upload. We will also upload the logo, home page layout we have in mind, and other supporting files.

NOTE: Please submit first the design of the home page. Based on this design we will ask selected designers to submit designs for the other pages.

Target Market(s)

Business people who want to share work related files with their colleagues

Industry/Entity Type

Business

Requirements
Must have
• All the required features are listed in the description of the website and specific pages that we will upload.

```html
<!DOCTYPE html>
<html lang="en">
<head>
<meta charset="utf-8">
<title>Gathr.io Blog</title>
<link href="https://fonts.googleapis.com/css2?family=Open+Sans:wght@400;600;700&display=swap" rel="stylesheet">
<style>
:root{
  --ink:#444;
  --muted:#666;
  --link:#1a6ea8;
  --orange:#f39a1f;
  --orange-dark:#e07f0c;
  --sky:#3d8fcc;
  --panel:#f3f3f3;
  --rule:#e2e2e2;
  --icon:#9a9a9a;
}
*{box-sizing:border-box;margin:0;padding:0}
html,body{width:1200px;height:1054px;overflow:hidden;background:#fff}
body{font-family:"Open Sans",Arial,sans-serif;color:var(--ink)}
.page{position:relative;width:1366px;height:1200px;transform:scale(.87848);transform-origin:0 0;
  background:linear-gradient(180deg,#fff 0,#fff 65px,var(--sky) 65px,#5fa5d9 160px,#bcdcf2 330px,#fff 430px)}
a{color:var(--link);text-decoration:none}
.abs{position:absolute}

.header{position:absolute;left:0;top:0;width:1366px;height:65px;background:linear-gradient(#fff,#efefef);border-bottom:1px solid #d4d4d4}
.brand{position:absolute;left:206px;top:12px;display:flex;align-items:center;gap:8px;font-size:25px;font-weight:600;color:#2a7fc0}
.brand-dot{width:28px;height:28px;border-radius:50%;background:#2a7fc0}
.social{display:flex;gap:10px}
.social i{display:block;width:14px;height:14px;border-radius:50%;background:var(--icon)}
.header .social{position:absolute;left:889px;top:27px}
.cta{position:absolute;left:989px;top:15px;width:175px;height:37px;border-radius:3px;background:linear-gradient(var(--orange),var(--orange-dark));border:1px solid #d77a0b;color:#fff;font-size:14px;font-weight:600;line-height:35px;padding-left:11px}
.cta::after{content:"";position:absolute;right:13px;top:14px;border-left:5px solid #fff;border-top:4px solid transparent;border-bottom:4px solid transparent}

.crumbs{position:absolute;left:204px;top:90px;font-size:12px;color:#d6e9f7}
.crumbs b{color:#fff;font-weight:600;margin-left:6px}
.crumbs span{margin-left:6px;font-size:8px;color:#9cc6e6}

.card{position:absolute;left:205px;top:128px;width:960px;height:1000px;background:#fff;border-radius:4px 4px 0 0}

.side-box{position:absolute;left:220px;width:175px;background:var(--panel);border-radius:2px;padding:8px 12px}
.side-box h3{font-size:15px;font-weight:400;color:#333;margin-bottom:10px}
.side-box a{display:block;font-size:13px;line-height:24px}

.main{position:absolute;left:413px;width:737px}
.meta{top:146px;font-size:11px;color:var(--muted)}
.meta a{color:var(--orange-dark)}
.title{top:166px;font-size:25px;line-height:29px;font-weight:700;color:#3c3c3c}
.byline{position:absolute;left:414px;top:232px;height:24px;padding:0 12px 0 9px;background:var(--panel);font-size:11px;line-height:24px;color:#555}
.body{font-size:13px;line-height:18px;color:#555}

.hero{position:absolute;left:414px;top:340px;width:736px;height:200px;overflow:hidden;
  background:linear-gradient(110deg,#7b2a5e 0,#c8416a 25%,#f07a2a 45%,#f5b71f 62%,#e9df2b 78%,#a2388c 100%)}
.hero-photo{position:absolute;left:31px;top:28px;width:142px;height:142px;border-radius:50%;border:6px solid #6d2b4f;background:linear-gradient(#8a6e5c,#4f7fae)}
.hero-box{position:absolute;left:197px;top:39px;width:436px;height:124px;background:rgba(40,28,22,.85);padding:14px 16px;color:#fff}
.hero-box h2{font-size:22px;font-weight:700;padding-bottom:8px;border-bottom:1px solid rgba(255,255,255,.3);width:350px}
.hero-box p{font-size:14px;line-height:17px;margin-top:8px}

.share-row{position:absolute;left:413px;top:703px;display:flex;align-items:center;font-size:13px}
.share-row .lbl{color:var(--link);margin-right:14px}
.btn-s{height:19px;border:1px solid #ccc;border-radius:2px;background:linear-gradient(#fff,#e8e8e8);font-size:11px;font-weight:600;padding:0 5px;line-height:17px;color:#333}
.count{height:19px;border:1px solid #ccc;background:#fff;font-size:11px;line-height:17px;padding:0 5px;margin:0 18px 0 4px}

.section{font-size:15px;font-weight:600;color:#333}
.rule{position:absolute;left:413px;width:737px;height:1px;background:var(--rule)}
.related{top:787px;font-size:13px;line-height:18px;font-weight:600;width:400px}
.related-date{top:829px;font-size:11px;color:var(--muted)}

.avatar{position:absolute;left:414px;top:913px;width:68px;height:66px;background:linear-gradient(#7a5a44,#c9a48a)}
.msg{position:absolute;left:493px;top:913px;width:654px;height:66px;border:1px solid #d8d8d8;border-radius:2px;background:#f7f7f7;font-size:11px;color:#555;padding:10px 13px}
.connect{position:absolute;left:496px;top:996px;font-size:12px;color:#555}
.connect .social{position:absolute;left:82px;top:2px;gap:12px}
.field{position:absolute;top:988px;width:191px;height:33px;border:1px solid #ccc;font-size:11px;line-height:31px;padding-left:10px;color:#666}
.post{position:absolute;left:1067px;top:988px;width:81px;height:33px;border:1px solid #c8c8c8;border-radius:2px;background:linear-gradient(#fff,#e6e6e6);font-size:12px;font-weight:600;line-height:31px;text-align:center;color:#555}

.footer-rule{position:absolute;left:205px;top:1148px;width:961px;height:1px;background:#d5d5d5}
.footer{position:absolute;left:205px;top:1163px;font-size:12px;color:#555}
.footer a{color:#555}
.footer a.on{color:var(--link)}
.copy{position:absolute;left:896px;top:1163px;font-size:12px;color:#555}
.footer-social{position:absolute;left:1093px;top:1164px}
</style>
</head>
<body>
<div class="page">
  <header class="header">
    <div class="brand"><span class="brand-dot"></span>Gathr.io</div>
    <div class="social"><i></i><i></i><i></i></div>
    <a class="cta" href="#">Access your shares</a>
  </header>

  <nav class="crumbs">Apps Marketplace<span>●</span><b>Nam liber tempor cum soluta nobis eleifend.</b></nav>

  <div class="card"></div>

  <aside class="side-box" style="top:140px;height:271px">
    <h3>Categories</h3>
    <a href="#">All Posts</a><a href="#">Commentary</a><a href="#">New Features</a><a href="#">Announcements</a><a href="#">Customer Stories</a><a href="#">How To</a><a href="#">Apps Marketplace</a><a href="#">Developers</a><a href="#">General</a>
  </aside>
  <aside class="side-box" style="top:428px;height:147px">
    <h3>Archives</h3>
    <a href="#">2012</a><a href="#">2011</a><a href="#">2010</a><a href="#">2009</a>
  </aside>

  <div class="main meta">Monday, September 17th, 2012 • <a href="#">12 Comments</a></div>
  <h1 class="main title">Nam liber tempor cum soluta nobis eleifend option congue nihil imperdiet doming id quod mazim.</h1>
  <div class="byline">By <a href="#">Mara Kessel</a>, Sr Product Marketing Manager, Platform</div>

  <p class="main body" style="top:265px">Lorem ipsum dolor sit amet, consectetuer adipiscing elit, sed diam nonummy nibh euismod tincidunt ut laoreet dolore magna aliquam erat volutpat, Ut wisi enim ad minim veniam, quis nostrud exerci tation ullamcorper suscipit lobortis nisl ut aliquip ex ea commodo consequat.</p>

  <div class="hero" role="img" aria-label="Banner with colourful feathers and a circular portrait of a user">
    <div class="hero-photo" role="img" aria-label="User portrait"></div>
    <div class="hero-box">
      <h2>I am a share</h2>
      <p>Create a share with files, pictures, or tasks on the fly for friends and colleagues</p>
    </div>
  </div>

  <p class="main body" style="top:557px">Duis autem vel eum iriure dolor in <a href="#">hendrerit in vulputate</a> velit esse molestie consequat, vel illum dolore eu feugiat nulla facilisis at vero eros et accumsan et iusto odio dignissim qui blandit praesent luptatum zzril delenit augue duis dolore te feugait nulla facilisi.</p>
  <p class="main body" style="top:628px">Claritas est etiam processus dynamicus, qui sequitur mutationem consuetudium lectorum. Mirum est notare quam littera gothica, quam nunc putamus parum claram, anteposuerit litterarum formas humanitatis per seacula quarta decima et quinta decima. Eodem modo typi, qui nunc nobis videntur parum clari, fiant sollemnes in futurum.</p>

  <div class="share-row">
    <span class="lbl">Share this</span>
    <span class="btn-s">Post</span><span class="count">8</span>
    <span class="btn-s">Plus</span><span class="count">1</span>
    <span class="btn-s">Like</span><span class="count">2</span>
    <span class="btn-s">Save</span><span class="count">5</span>
  </div>

  <h2 class="main section" style="top:746px">Related Posts</h2>
  <div class="rule" style="top:776px"></div>
  <a class="main related" href="#">Typi non habent claritatem insitam; est usus legentis in iis qui facit eoruclaritatem.</a>
  <div class="main related-date">Monday, September 17th, 2012</div>

  <h2 class="main section" style="top:867px">0 Comments</h2>
  <div class="rule" style="top:897px"></div>
  <div class="avatar" role="img" aria-label="Commenter avatar photo"></div>
  <div class="msg">Enter your message here...</div>
  <div class="connect">Connect with <div class="social"><i></i><i></i><i></i></div></div>
  <div class="field" style="left:667px">Username</div>
  <div class="field" style="left:868px">Email</div>
  <div class="post">Post</div>
  <div class="rule" style="top:1031px"></div>

  <div class="footer-rule"></div>
  <footer class="footer"><a href="#">Home</a> | <a href="#">About us</a> | <a class="on" href="#">Product Tour</a> | <a href="#">Free for Unlimited Users</a> | <a href="#">Terms of use</a> | <a href="#">Jobs</a> | <a href="#">Sign up</a> | <a href="#">Blog</a> |<a href="#">Press</a> | <a href="#">Contact us</a></footer>
  <div class="copy">Copyright © 2012 Gathr.io</div>
  <div class="social footer-social"><i></i><i></i><i></i></div>
</div>
</body>
</html>
```